Heron Freightlines needs Bussiness cards!

Our new trucking company needs business cards!
We need the same design with two different names and emails, everything else it's the same.
I have included our original logo so we can use it for the design.
Note: the logo to be used is the o e with the buffalo on the right side, next to the letters H and F.

Target Market(s)

Trucking, refrigerated transportation, freight

Industry/Entity Type

Business

Contact Information for Business Card

Card #1:
Marcus Tellwright
marcustellwright@heronfreightlines.example
1-844-555-0193
(956)555-0178
3817 W. Tarrow Ave.
Pharr, TX 78599
www.heronfreightlines.example

Card#2:
Orla Brennick
orla@heronfreightlines.example
1-844-555-0193
(956)555-0178
3817 W. Tarrow Ave.
Pharr, TX 78599
www.heronfreightlines.example

Font styles to use
Sans Serif

Colors
0655a3
ec1f27
ffffff

Requirements
Must have
• our logo
Nice to have
• roads on background,

```html
<!DOCTYPE html>
<html lang="en">
<head>
<meta charset="utf-8">
<title>Heron Freightlines – Business Card</title>
<link rel="stylesheet" href="https://fonts.googleapis.com/css2?family=Open+Sans:wght@400;700&family=Noto+Serif:wght@400&display=swap">
<style>
  :root {
    --frame: #000000;
    --brand-blue: #0655a3;
    --brand-red: #ec1f27;
    --name-grey: #6b6b6b;
    --ink: #111111;
    --address-ink: #333333;
    --url-ink: #444444;
    --sheen-light: #ffffff;
    --sheen-mid: #d6d6d6;
    --sheen-dark: #b5b5b5;
  }
  html, body {
    margin: 0;
    padding: 0;
    width: 1200px;
    height: 686px;
    overflow: hidden;
    background: #ffffff;
  }
  .card {
    position: relative;
    box-sizing: border-box;
    width: 1200px;
    height: 686px;
    border: 10px solid var(--frame);
    background: linear-gradient(
      to bottom,
      var(--sheen-light) 0%,
      #f4f4f4 10%,
      var(--sheen-mid) 28%,
      var(--sheen-dark) 44%,
      var(--sheen-mid) 52%,
      #f7f7f7 62%,
      var(--sheen-light) 70%,
      var(--sheen-mid) 84%,
      var(--sheen-dark) 100%
    );
    font-family: "Open Sans", Arial, sans-serif;
  }
  .website {
    position: absolute;
    top: 14px;
    right: 13px;
    margin: 0;
    font-family: "Noto Serif", Georgia, serif;
    font-size: 19px;
    color: var(--url-ink);
  }
  .holder-name {
    position: absolute;
    left: 41px;
    top: 45px;
    margin: 0;
    font-weight: 400;
    font-size: 52px;
    line-height: 1;
    color: var(--name-grey);
  }
  .contact-lines {
    position: absolute;
    left: 41px;
    top: 133px;
    margin: 0;
    font-size: 40px;
    line-height: 48px;
    color: var(--ink);
    letter-spacing: -0.3px;
  }
  .contact-lines span { display: block; }
  .address {
    position: absolute;
    left: 41px;
    top: 556px;
    margin: 0;
    font-family: "Noto Serif", Georgia, serif;
    font-style: normal;
    font-size: 29px;
    line-height: 38px;
    color: var(--address-ink);
  }
  .brand-mark {
    position: absolute;
    right: 34px;
    top: 552px;
    display: flex;
    align-items: center;
    gap: 14px;
  }
  .brand-dot {
    width: 42px;
    height: 42px;
    border-radius: 50%;
    background: var(--brand-red);
  }
  .brand-name {
    font-size: 40px;
    font-weight: 700;
    color: var(--brand-blue);
    line-height: 1;
  }
</style>
</head>
<body>
  <div class="card">
    <p class="website">www.heronfreightlines.example</p>
    <h1 class="holder-name">Marcus Tellwright</h1>
    <p class="contact-lines">
      <span class="email">marcustellwright@heronfreightlines.example</span>
      <span class="phone-tollfree">1-844-555-0193</span>
      <span class="phone-local">(956)555-0178</span>
    </p>
    <address class="address">3817 W. Tarrow Ave.<br>Pharr, TX 78599</address>
    <div class="brand-mark">
      <span class="brand-dot"></span>
      <span class="brand-name">Heron Freightlines</span>
    </div>
  </div>
</body>
</html>
```